E-commerce website for interior joinery product - Furnvale Trade

we want to create a E-commerce website to list our modular products.
other than E-commerce functions, we will also require membership logins and setting different price tiers for B2B customers (construction company and home building groups. for logos and our products etc please visit www.furnvale.co.nz
You can also get some ideas from https://brontecabinets.co.nz/ready-to-order/

Number of Pages Required

5+ page

Requirements
Must have
• on the product page, the customer can have the option to choose different colours and upgradable options.

```html
<!DOCTYPE html>
<html lang="en">
<head>
<meta charset="utf-8">
<title>Shop – Furnvale Trade</title>
<link href="https://fonts.googleapis.com/css2?family=Hind:wght@400;500;600&family=Merriweather:wght@700&family=Montserrat:wght@600&display=swap" rel="stylesheet">
<style>
:root{
  --green:#7dbb42;
  --ink:#1d2a33;
  --text:#3a3a3a;
  --muted:#8a8a8a;
  --page:#f4f4f4;
  --panel:#ffffff;
  --band:#021623;
  --footer:#f9f9f9;
  --line:#e6e6e6;
}
*{margin:0;padding:0;box-sizing:border-box}
html,body{width:906px;height:1200px;overflow:hidden}
body{position:relative;background:var(--page);font-family:'Hind',sans-serif;color:var(--text)}
.abs{position:absolute}
.site-header{left:0;top:0;width:906px;height:54px;background:#fff;border-bottom:1px solid var(--line)}
.brand{display:flex;align-items:center;gap:6px;font-family:'Hind',sans-serif;font-weight:500;color:#5d6b73}
.brand-mark{width:16px;height:16px;background:#5d6b73}
.header-brand{left:125px;top:16px;font-size:17px}
.nav{top:20px;font-size:9.5px;color:var(--ink);line-height:12px}
.nav.active{color:var(--green)}
.caret{font-size:7px;margin-left:3px}
.cart{left:767px;top:18px;width:16px;height:17px;border:1.5px solid var(--green);border-radius:2px;font-size:8px;color:var(--green);text-align:center;line-height:15px;font-weight:600}
.content{left:113px;top:91px;width:679px;height:740px;background:var(--panel)}
.crumbs{left:174px;top:141px;font-size:8px;color:#6b6b6b}
.page-title{left:174px;top:161px;font-family:'Merriweather',serif;font-size:18px;color:var(--green)}
.result-count{left:174px;top:202px;font-size:9.5px}
.sorting{left:605px;top:200px;width:127px;height:24px;border:1px solid #ddd;font-size:9.5px;color:#555;padding:6px 7px;line-height:12px}
.sorting span{position:absolute;right:6px;top:7px;font-size:6px}
.product-photo{width:178px;height:178px}
.sale{width:27px;height:27px;border-radius:50%;background:var(--green);font-size:8.5px;color:#1c1c1c;text-align:center;line-height:28px}
.cat{font-size:7.5px;color:var(--muted)}
.name{font-family:'Merriweather',serif;font-size:9.5px;color:var(--ink)}
.stars{height:9px;width:42px}
.price{font-size:8.5px;font-weight:600;color:var(--ink)}
.price s{color:var(--muted);font-weight:400;margin-right:3px}
.cta-band{left:0;top:867px;width:906px;height:101px;background:var(--band)}
.cta-title{left:113px;top:904px;font-family:'Merriweather',serif;font-size:15.5px;color:#fff}
.cta-btn{left:576px;top:906px;width:105px;height:28px;border-radius:14px;background:var(--green);color:#fff;font-family:'Montserrat',sans-serif;font-size:8.5px;text-align:center;line-height:28px;letter-spacing:.3px}
.site-footer{left:0;top:968px;width:906px;height:232px;background:var(--footer)}
.footer-brand{left:132px;top:1084px;font-size:19px}
.footer-brand .brand-mark{width:20px;height:20px}
.f-head{font-family:'Montserrat',sans-serif;font-size:9.5px;letter-spacing:1.3px;color:#7a7a7a;width:160px;text-align:center}
.f-link{font-size:9.5px;color:var(--ink);width:160px;text-align:center}
.branch{left:628px;font-size:9.5px;color:var(--ink)}
.branch.tel{color:var(--green)}
</style>
</head>
<body>
<svg width="0" height="0" style="position:absolute">
  <defs>
    <symbol id="star" viewBox="0 0 10 10"><path d="M5 .8l1.2 2.7 2.9.3-2.2 1.9.7 2.9L5 7.1 2.4 8.6l.7-2.9L.9 3.8l2.9-.3z" fill="none" stroke="#7dbb42" stroke-width=".8"/></symbol>
  </defs>
</svg>

<header class="site-header abs">
  <div class="brand header-brand abs"><span class="brand-mark"></span>Furnvale Trade</div>
  <span class="nav abs" style="left:495px">Home</span>
  <span class="nav active abs" style="left:539px">Products<span class="caret">⌵</span></span>
  <span class="nav abs" style="left:606px">Gallery</span>
  <span class="nav abs" style="left:653px">Contact</span>
  <span class="nav abs" style="left:704px">Account<span class="caret">⌵</span></span>
  <div class="cart abs">0</div>
</header>

<main class="content abs"></main>
<div class="crumbs abs">Home / Shop</div>
<h1 class="page-title abs">Shop</h1>
<div class="result-count abs">Showing all 4 results</div>
<div class="sorting abs">Default sorting<span>▼</span></div>

<div class="product-photo abs" style="left:174px;top:247px;background:linear-gradient(90deg,#8e969c,#d7d4d0 25%,#6f6a68 50%,#c8b8a6 75%,#a5abae)" role="img" aria-label="Bi-fold wardrobe doors photo"></div>
<div class="product-photo abs" style="left:363px;top:247px;background:linear-gradient(180deg,#f1f0ec 0%,#e9e8e4 75%,#b89773 100%)" role="img" aria-label="White hinged wardrobe doors photo"></div>
<div class="product-photo abs" style="left:552px;top:247px;background:linear-gradient(90deg,#2f2b29,#4a4340 50%,#2f2b29)" role="img" aria-label="Dark melamine sliding doors photo"></div>
<div class="product-photo abs" style="left:174px;top:510px;background:linear-gradient(180deg,#eeeeec 0%,#c9c8c4 55%,#7b5d44 100%)" role="img" aria-label="Glass room divider in bedroom photo"></div>

<div class="sale abs" style="left:329px;top:242px">Sale!</div>
<div class="sale abs" style="left:518px;top:242px">Sale!</div>
<div class="sale abs" style="left:708px;top:242px">Sale!</div>
<div class="sale abs" style="left:329px;top:505px">Sale!</div>

<div class="cat abs" style="left:174px;top:433px">Bi-fold Doors</div>
<div class="name abs" style="left:174px;top:445px">Bi-fold Doors</div>
<svg class="stars abs" style="left:174px;top:461px"><use href="#star" x="0" width="8" height="8"/><use href="#star" x="8" width="8" height="8"/><use href="#star" x="16" width="8" height="8"/><use href="#star" x="24" width="8" height="8"/><use href="#star" x="32" width="8" height="8"/></svg>
<div class="price abs" style="left:174px;top:473px"><s>$890.00</s>$765.00</div>

<div class="cat abs" style="left:363px;top:433px">Doors</div>
<div class="name abs" style="left:363px;top:445px">Hinge Doors</div>
<svg class="stars abs" style="left:363px;top:461px"><use href="#star" x="0" width="8" height="8"/><use href="#star" x="8" width="8" height="8"/><use href="#star" x="16" width="8" height="8"/><use href="#star" x="24" width="8" height="8"/><use href="#star" x="32" width="8" height="8"/></svg>
<div class="price abs" style="left:363px;top:473px"><s>$789.00</s>$765.00</div>

<div class="cat abs" style="left:552px;top:433px">Doors</div>
<div class="name abs" style="left:552px;top:445px">Melamine Sliding Doors</div>
<svg class="stars abs" style="left:552px;top:461px"><use href="#star" x="0" width="8" height="8"/><use href="#star" x="8" width="8" height="8"/><use href="#star" x="16" width="8" height="8"/><use href="#star" x="24" width="8" height="8"/><use href="#star" x="32" width="8" height="8"/></svg>
<div class="price abs" style="left:552px;top:473px"><s>$800.00</s>$750.00</div>

<div class="cat abs" style="left:174px;top:696px">Doors</div>
<div class="name abs" style="left:174px;top:708px">Room Divider</div>
<svg class="stars abs" style="left:174px;top:724px"><use href="#star" x="0" width="8" height="8"/><use href="#star" x="8" width="8" height="8"/><use href="#star" x="16" width="8" height="8"/><use href="#star" x="24" width="8" height="8"/><use href="#star" x="32" width="8" height="8"/></svg>
<div class="price abs" style="left:174px;top:736px"><s>$555.00</s>$543.00</div>

<section class="cta-band abs"></section>
<h2 class="cta-title abs">Looking to renovate your wardrobe?</h2>
<div class="cta-btn abs">SHOP NOW</div>

<footer class="site-footer abs"></footer>
<div class="brand footer-brand abs"><span class="brand-mark"></span>Furnvale Trade</div>

<div class="f-head abs" style="left:288px;top:1019px">QUICK LINKS</div>
<div class="f-link abs" style="left:288px;top:1052px">Home</div>
<div class="f-link abs" style="left:288px;top:1078px">Products</div>
<div class="f-link abs" style="left:288px;top:1104px">Gallery</div>
<div class="f-link abs" style="left:288px;top:1130px">Buyer’s Guide</div>

<div class="f-head abs" style="left:458px;top:1019px">PRODUCTS</div>
<div class="f-link abs" style="left:458px;top:1052px">Doors</div>
<div class="f-link abs" style="left:458px;top:1078px">Wardrobe System</div>
<div class="f-link abs" style="left:458px;top:1104px">Storage Space</div>
<div class="f-link abs" style="left:458px;top:1130px">Accessories</div>

<div class="f-head abs" style="left:627px;top:1019px">OUR BRANCHES</div>
<div class="branch abs" style="top:1047px">Auckland Showroom</div>
<div class="branch tel abs" style="top:1064px">09 555 0148</div>
<div class="branch abs" style="top:1080px">Hamilton Showroom</div>
<div class="branch tel abs" style="top:1097px">07 555 0273</div>
</body>
</html>
```